Local Newspaper Quarterly " Meet The Realtor" print ad

I need a new add made up. This was my last ad:
http://www.harborlinepressads.example/static/pdfs/agents1309/Ar092213%20G10%20006%20Prepress.pdf

I do not really care of Realtor advertisements because they are just so cheesy and rather pompous-like. However, it's a necessary evil
My ads have always been outside of the box and/or visually sharp.
I now have a new company' Voske Real Estate( I will attach a logo) contact info:
Carl Voske
Voske Real Estate
Broker/Owner( this can be somewhere in small print or corner of ad since it's mandatory to have shown
Phone: 304-555-0194
Email: Carl@VoskeRealEstate.Example
VoskeRealEstate.Example
I would like social icons(FL,Chirpr, Pinmosaic! Dwello, Qlink)

Ideas: In my logo font or using the image at the top I envision
Something like:
A
Voske Real Estate
Of Mind
Body of ad?
Images of Charleston WV as a real light back ground
With 3 or 4 customer reviews chosen by you in this site:
http://webcarl.example/think.html

Bottom: contact info and my name in a nice Signature style ??
My agent pic at the bottom right( to be small. I don't want my big head overshadowing the message)

I have yet to think of a tagline for my new company:
I have been thinking of " Luxury Services For All Things Real Estate"

Or nothing at all ??? I don't care for tag lines but then again that's part of the business

Target Market(s)

Higher end homes

Industry/Entity Type

Business

Colors
0f59a5
0392cd
0f0f0f
eaeaea
ffffff

Requirements
Must have
• My logo and colors
Nice to have
• My agent picture and client review.
Should not have
• No typical real estate images like a house or home buyer

```html
<!DOCTYPE html>
<html lang="en">
<head>
<meta charset="utf-8">
<title>Voske Real Estate – Meet The Realtor</title>
<link href="https://fonts.googleapis.com/css2?family=Montserrat:wght@400;500;600&family=Arimo:wght@400;700&family=Italianno&display=swap" rel="stylesheet">
<style>
  :root {
    --band-dark: #2e2c2d;
    --band-light: #ebeae5;
    --ink: #0f0f0f;
    --muted: #d9cfc0;
    --brand-blue: #0f59a5;
    --brand-cyan: #0392cd;
    --white: #ffffff;
    --sky: #e4e6e8;
  }
  * { margin: 0; padding: 0; box-sizing: border-box; }
  html, body { width: 1200px; height: 912px; overflow: hidden; background: var(--white); }
  .ad { position: relative; width: 1200px; height: 912px; overflow: hidden; font-family: "Arimo", Arial, sans-serif; color: var(--ink); }

  .masthead { position: absolute; left: 0; top: 0; width: 1200px; height: 148px; background: var(--band-dark); }
  .brand { position: absolute; left: 62px; top: 50px; display: flex; align-items: center; gap: 12px; }
  .brand-mark { width: 26px; height: 26px; border-radius: 50%; background: var(--brand-cyan); }
  .brand-name { font-family: "Montserrat", sans-serif; font-weight: 600; font-size: 30px; color: var(--brand-cyan); letter-spacing: 1px; }

  .social { position: absolute; right: 28px; top: 88px; display: flex; gap: 22px; list-style: none; }
  .social li { width: 48px; height: 48px; border-radius: 6px; display: flex; align-items: center; justify-content: center;
    font-family: "Arimo", sans-serif; font-weight: 700; font-size: 9px; color: var(--white); }
  .social .dwello { background: #7cb342; }
  .social .fl { background: #3b5c9a; }
  .social .chirpr { background: #29a9df; border-radius: 50%; }
  .social .pinmosaic { background: #cb2027; }
  .social .qlink { background: #d14836; }

  .tagline { position: absolute; left: 0; top: 148px; width: 1200px; height: 70px; background: var(--band-light);
    display: flex; align-items: center; justify-content: center;
    font-family: "Montserrat", sans-serif; font-weight: 400; font-size: 40px; letter-spacing: 1.5px; color: var(--ink); }

  .cityscape { position: absolute; left: 0; top: 218px; width: 1200px; height: 572px;
    background: linear-gradient(180deg, #eceef0 0%, #e3e5e6 30%, #d9dad6 55%, #cfd3c9 75%, #d7dcd6 100%); }

  .review { position: absolute; }
  .review h2 { font-family: "Arimo", Arial, sans-serif; font-weight: 700; font-size: 25px; margin-bottom: 8px; }
  .review p { font-size: 16.5px; line-height: 22px; }
  .r1 { left: 40px; top: 243px; width: 600px; }
  .r2 { left: 572px; top: 362px; width: 600px; }
  .r3 { left: 44px; top: 487px; width: 560px; }
  .r4 { left: 573px; top: 615px; width: 580px; }

  .footer { position: absolute; left: 0; top: 790px; width: 1200px; height: 122px; background: var(--band-dark); }
  .web-block { position: absolute; left: 8px; top: 28px; width: 382px; height: 68px;
    border-top: 2px solid var(--muted); border-bottom: 2px solid var(--muted);
    display: flex; flex-direction: column; justify-content: center; align-items: center;
    font-family: "Montserrat", sans-serif; font-size: 19px; letter-spacing: 2px; color: var(--muted); line-height: 28px; }
  .phone { position: absolute; left: 424px; top: 38px; font-family: "Montserrat", sans-serif; font-size: 38px; letter-spacing: 8px; color: var(--muted); }
  .signature { position: absolute; left: 820px; top: 14px; font-family: "Italianno", cursive; font-size: 44px; color: var(--muted); }
  .title-block { position: absolute; left: 824px; top: 66px; font-family: "Montserrat", sans-serif; font-weight: 500;
    font-size: 17px; line-height: 24px; letter-spacing: 1.5px; font-variant: small-caps; color: var(--muted); }

  .agent-photo { position: absolute; left: 1015px; top: 743px; width: 157px; height: 161px;
    border: 2px solid #bdbdbd; background: linear-gradient(135deg, #c9822e 0%, #8a6a2a 40%, #d8d8d2 75%, #efe9df 100%); }
</style>
</head>
<body>
<div class="ad">
  <header class="masthead">
    <div class="brand">
      <span class="brand-mark"></span>
      <span class="brand-name">Voske Real Estate</span>
    </div>
    <ul class="social">
      <li class="dwello">Dwello</li>
      <li class="fl">FL</li>
      <li class="chirpr">Chirpr</li>
      <li class="pinmosaic">Pinmosaic</li>
      <li class="qlink">Qlink</li>
    </ul>
  </header>

  <div class="tagline">LUXURY SERVICES FOR ALL THINGS REAL ESTATE</div>

  <div class="cityscape" role="img" aria-label="Faded photograph of the Charleston, WV skyline and river with a bridge"></div>

  <section class="review r1">
    <h2>Walter J. Pruett</h2>
    <p>Carl was fantastic. He knew exactly what I was looking for and found the absolute perfect house for me. Truly an asset to his company!</p>
  </section>
  <section class="review r2">
    <h2>Kendra Lusk</h2>
    <p>Carl did an extraordinary job with me and made my first-time home-buying experience a cinch! I have and will continue to refer people to CARL VOSKE! If they don’t take my advice, it’s their loss!</p>
  </section>
  <section class="review r3">
    <h2>Dr. Alan Merriwether</h2>
    <p>Carl Voske is an OUTSTANDING Real Estate Agent. He helped with many aspects of the purchase that made it an exceptional experience.</p>
  </section>
  <section class="review r4">
    <h2>Tessa Colwell</h2>
    <p>Carl was excellent throughout the whole process! Always available to answer questions and to calm me down when things went haywire with my loan. I will not hesitate to recommend Carl.<br>Great Job!</p>
  </section>

  <footer class="footer">
    <div class="web-block">
      <span>VoskeRealEstate.Example</span>
      <span>Carl@VoskeRealEstate.Example</span>
    </div>
    <div class="phone">304-555-0194</div>
    <div class="signature">Carl Voske</div>
    <div class="title-block">Voske Real Estate<br>Broker/Owner</div>
  </footer>

  <div class="agent-photo" role="img" aria-label="Small portrait of agent Carl Voske against autumn foliage"></div>
</div>
</body>
</html>
```